A label for my commercially sold local honey. This is a LABEL not a logo

3 inches high
2 inches wide

Target Market(s)

Customers who like "local" honey

Logo Text

Wildflower Honey -- 100% Pure & Unfiltered -- Florida

Logo styles of interest
Wordmark Logo
Requirements
Must have
• Wildflower Honey -- 100% Pure & Unfiltered -- Florida

Florida should be dominant

3 inches high / 2 inches wide

```html
<!DOCTYPE html>
<html lang="en">
<head>
<meta charset="utf-8">
<title>Wildflower Honey Label</title>
<link rel="stylesheet" href="https://fonts.googleapis.com/css2?family=Ribeye&family=Montserrat:wght@800&family=Questrial&display=swap">
<style>
  :root {
    --kraft: #d4a67c;
    --kraft-light: #ddb48c;
    --kraft-dark: #c49468;
    --forest: #3c4834;
    --forest-deep: #333e2c;
    --honey-tan: #d3a885;
    --box-top: #deb590;
    --box-bottom: #a6764f;
    --ink: #394533;
    --white: #ffffff;
  }
  * { margin: 0; padding: 0; box-sizing: border-box; }
  html, body { width: 800px; height: 1200px; overflow: hidden; background: var(--kraft); }
  .label {
    position: relative;
    width: 800px;
    height: 1200px;
    background: radial-gradient(ellipse at 50% 40%, var(--kraft-light), var(--kraft) 60%, var(--kraft-dark));
    overflow: hidden;
  }
  .label-art { position: absolute; inset: 0; }
  .brand-seal {
    position: absolute;
    left: 267px; top: 115px;
    width: 266px; height: 266px;
    border-radius: 50%;
    background: var(--kraft-light);
    box-shadow: 0 6px 14px rgba(0,0,0,0.35);
    display: flex; align-items: center; justify-content: center;
    text-align: center;
  }
  .brand-name {
    font-family: "Questrial", sans-serif;
    font-size: 34px;
    line-height: 1.1;
    color: var(--forest);
    letter-spacing: 1px;
  }
  .product-name {
    position: absolute;
    left: 0; right: 0; top: 0;
    text-align: center;
  }
  .product-name .variety {
    position: absolute;
    left: 0; right: 0; top: 412px;
    font-family: "Ribeye", cursive;
    font-size: 114px;
    line-height: 1;
    color: var(--white);
    text-shadow: 0 4px 6px rgba(0,0,0,0.35);
  }
  .product-name .kind {
    position: absolute;
    left: 0; right: 0; top: 540px;
    font-family: "Montserrat", sans-serif;
    font-weight: 800;
    font-size: 84px;
    line-height: 1;
    color: var(--honey-tan);
    letter-spacing: 2px;
  }
  .purity-panel {
    position: absolute;
    left: 226px; top: 680px;
    width: 348px; height: 298px;
    background: linear-gradient(180deg, var(--box-top), var(--box-top) 30%, var(--box-bottom));
    box-shadow: 0 4px 10px rgba(0,0,0,0.25);
    font-family: "Questrial", sans-serif;
    color: var(--ink);
  }
  .purity-panel .percent {
    display: block;
    margin-top: 68px;
    padding-left: 38px;
    font-size: 104px;
    line-height: 1;
  }
  .purity-panel .claim {
    display: block;
    padding-left: 38px;
    font-size: 34px;
    line-height: 1.02;
    letter-spacing: 6px;
    margin-top: 2px;
  }
  .purity-panel .amp { font-style: italic; font-size: 30px; letter-spacing: 0; }
  .origin {
    position: absolute;
    left: 0; right: 0; top: 1032px;
    padding-left: 30px;
    text-align: center;
    font-family: "Questrial", sans-serif;
    font-size: 134px;
    line-height: 1;
    letter-spacing: 30px;
    color: var(--ink);
  }
</style>
</head>
<body>
  <main class="label">
    <svg class="label-art" width="800" height="1200" viewBox="0 0 800 1200" xmlns="http://www.w3.org/2000/svg">
      <defs>
        <linearGradient id="flowerTone" x1="0" y1="0" x2="0" y2="1">
          <stop offset="0" stop-color="#c9996e" stop-opacity="0.55"/>
          <stop offset="1" stop-color="#c9996e" stop-opacity="0.15"/>
        </linearGradient>
      </defs>
      <g class="flower-field">
        <rect role="img" aria-label="Line illustration of daisies" x="0" y="690" width="226" height="360" fill="url(#flowerTone)"/>
        <rect role="img" aria-label="Line illustration of daisies" x="574" y="690" width="226" height="360" fill="url(#flowerTone)"/>
        <rect role="img" aria-label="Line illustration of small daisies" x="226" y="978" width="348" height="50" fill="url(#flowerTone)"/>
      </g>
      <path class="title-band" d="M0 284 H800 V744 Q400 610 0 748 Z" fill="var(--forest)"/>
      <rect class="honeycomb-strip" role="img" aria-label="Honeycomb line pattern" x="0" y="208" width="800" height="76" fill="var(--forest-deep)" opacity="0.25"/>
    </svg>

    <div class="brand-seal">
      <span class="brand-name">Sawgrass<br>Hive</span>
    </div>

    <h1 class="product-name">
      <span class="variety">Wildflower</span>
      <span class="kind">HONEY</span>
    </h1>

    <div class="purity-panel">
      <span class="percent">100%</span>
      <span class="claim">PURE <span class="amp">&amp;</span><br>UNFILTERED</span>
    </div>

    <p class="origin">FLORIDA</p>
  </main>
</body>
</html>
```